Bright Harbor Capital website

Build a website template for the Bright Harbor Capital fund.
Looking for a cool website design showing companies we are using the latest in web design trends. We want to attract app developers, typically the younger set.
A good example of one of our competitive firms is http://tallmeadowfund.example
The required components for the website include:
1) Funding application
2) about our firm
a) Partner profiles - We will include photographs and bios about each of the partners in our firm.
b) Invest with Bright Harbor - This will include information how to invest with our fund
c) our process - About our process for evaluating, funding and helping build successful businesses - This will include a narrative about the target companies, how we work, the type of deals we are interested in, our expectations, etc ...
3) Investment profiles - Stories about the companies we invest with
4) News - Output from our twitter feed and copies of our Blog posts

```html
<!DOCTYPE html>
<html lang="en">
<head>
<meta charset="utf-8">
<title>Bright Harbor Capital</title>
<link href="https://fonts.googleapis.com/css2?family=Open+Sans:wght@300;400;600;700&display=swap" rel="stylesheet">
<style>
:root{
  --bg-outer:#2b2b2b;
  --page:#ffffff;
  --green:#6aaa1e;
  --text:#4a4a4a;
  --border:#e3e3e3;
  --orange:#f28a12;
  --btn-gray:#868b8f;
  --footer:#1e1e1e;
  --footer-text:#b5b5b5;
  --dark-btn:#2a2a2a;
}
*{box-sizing:border-box;margin:0;padding:0}
html,body{width:763px;height:1200px;overflow:hidden}
body{background:var(--bg-outer);font-family:'Open Sans',sans-serif;color:var(--text);position:relative}
.page{position:absolute;left:70px;top:10px;width:623px;height:934px;background:var(--page)}
.header{position:absolute;left:0;top:0;width:623px;height:86px;border-top:2px solid var(--green);background:linear-gradient(120deg,#fff 0%,#f3f5f1 60%,#eef1eb 100%)}
.header-notch{position:absolute;left:550px;top:0;width:0;height:0;border-left:12px solid transparent;border-right:12px solid transparent;border-top:10px solid var(--green)}
.brand{position:absolute;left:16px;top:28px;display:flex;align-items:center;gap:8px}
.brand-mark{width:26px;height:26px;border-radius:50%;background:var(--green)}
.brand-name{font-size:21px;font-weight:600;color:var(--green);letter-spacing:-.2px;white-space:nowrap}
.contact-phone{position:absolute;left:367px;top:41px;font-size:7.5px;color:#777;display:flex;align-items:center;gap:3px;white-space:nowrap}
.social{position:absolute;left:454px;top:35px;display:flex;gap:2px}
.social span{width:20px;height:20px;border:1px solid #ddd;background:#f7f7f7}
.nav{position:absolute;left:0;top:86px;width:623px;height:29px;background:var(--green);display:flex;justify-content:space-between;padding-right:8px;font-size:7.9px;color:#fff;align-items:center}
.nav a{flex:none;white-space:nowrap;color:#fff;text-decoration:none;padding:0 4px;height:29px;line-height:29px}
.nav a.active{background:#5b5f63;padding:0 13px}
.tagline{position:absolute;left:0;top:140px;width:623px;text-align:center;font-size:13.4px;font-weight:300;color:#555;line-height:21px;white-space:nowrap}
.tagline strong{color:var(--green);font-weight:400}
.rule{position:absolute;left:45px;top:200px;width:539px;height:1px;background:#ddd}
.hero{position:absolute;left:0;top:216px;width:623px;height:248px;background:linear-gradient(90deg,#f4f4f4,#ececec)}
.hero-photo{position:absolute;left:14px;top:10px;width:332px;height:238px;background:linear-gradient(135deg,#d9c4b0 0%,#b89b84 45%,#8d98a6 100%);border-radius:4px 4px 0 0}
.hero-shadow{position:absolute;left:80px;top:474px;width:603px;height:10px;background:radial-gradient(ellipse at top,rgba(0,0,0,.25),transparent 70%)}
.hero-copy{position:absolute;left:372px;top:54px;width:236px}
.hero-copy h1{font-size:20px;font-weight:300;line-height:21px;color:#333;white-space:nowrap}
.hero-copy h1 b{font-weight:600}
.hero-copy p{margin-top:16px;font-size:10.4px;line-height:13px;color:#333}
.btn-orange{margin-top:17px;display:flex;align-items:center;justify-content:space-between;width:154px;height:32px;padding:0 10px;background:var(--orange);color:#fff;font-size:10px;border-radius:2px;white-space:nowrap}
.btn-orange svg{width:20px;height:20px}
.features{position:absolute;left:70px;top:538px;width:623px}
.feature{position:absolute;top:0;width:124px}
.feature-head{display:flex;gap:7px;align-items:flex-start}
.feature-icon{width:32px;height:32px;border:2px solid #ddd;border-radius:50%;flex:none}
.feature-title{border-left:1px solid #ddd;padding-left:6px;font-size:9.2px;color:#333;line-height:12px;white-space:nowrap}
.feature-title small{display:block;font-size:7.4px;color:#aaa}
.feature p{margin-top:13px;font-size:8.4px;line-height:11.5px;color:#aaa}
.btn-gray{display:inline-block;margin-top:12px;width:65px;height:22px;line-height:22px;text-align:center;background:var(--btn-gray);color:#fff;font-size:8.8px;border-bottom:2px solid #5e6266;white-space:nowrap}
.section-rule{position:absolute;left:12px;top:702px;width:599px;height:1px;background:#eee}
.section-title{position:absolute;font-size:16px;font-weight:300;color:#444;white-space:nowrap}
.post{position:absolute;top:770px;width:150px}
.post-head{display:flex;gap:6px}
.post-date{width:20px;text-align:center;flex:none}
.post-date .day{display:block;height:22px;line-height:22px;background:#f0f0f0;font-size:11px;color:#444}
.post-date .mon{display:block;background:var(--green);color:#fff;font-size:7px;line-height:9px}
.post-title{font-size:11.2px;font-weight:300;color:#777;line-height:14.5px}
.post p{margin-top:22px;font-size:7.8px;line-height:12.8px;color:#999}
.request{position:absolute;left:404px;top:753px;width:205px;height:160px;border:1px solid var(--border);padding:4px}
.field{background:#ececec;font-size:7.8px;color:#666;padding:0 8px;margin-bottom:4px}
.field.short{height:25px;line-height:25px}
.field.tall{height:63px;padding-top:8px}
.btn-submit{display:inline-block;width:65px;height:22px;line-height:22px;text-align:center;background:var(--dark-btn);color:#fff;font-size:9.6px;font-weight:600;margin-top:2px}
.footer{position:absolute;left:70px;top:944px;width:623px;height:216px;background:var(--footer);color:var(--footer-text);font-size:7.4px}
.footer-col{position:absolute;top:24px;width:155px}
.footer-col h3{font-size:7.8px;color:#fff;font-weight:600;padding-bottom:9px;border-bottom:1px solid #333;margin-bottom:12px}
.footer-col p{line-height:11.5px}
.contact-line{padding:9px 0;border-bottom:1px solid #2e2e2e;color:#ccc;white-space:nowrap}
.contact-line b{color:#ddd}
.recent li{list-style:none;margin-bottom:11px;color:#ddd;white-space:nowrap}
.recent li small{display:block;color:#888;font-size:6.6px;margin-top:4px}
.tweet{display:flex;gap:8px;margin-bottom:15px;line-height:11.5px;color:#ddd}
.tweet-dot{width:12px;height:12px;border-radius:50%;background:#fff;flex:none;margin-top:1px}
.copyright{position:absolute;left:0;top:1174px;width:763px;text-align:center;font-size:7.8px;color:#ccc}
</style>
</head>
<body>
<div class="page">
  <header class="header">
    <div class="header-notch"></div>
    <div class="brand"><span class="brand-mark"></span><span class="brand-name">Bright Harbor Capital</span></div>
    <div class="contact-phone">
      <svg width="7" height="7" viewBox="0 0 10 10"><path d="M2 1l2 2-1 1.5c.6 1.2 1.4 2 2.5 2.5L7 6l2 2-1.5 1.5C4.5 9 1 5.5.5 2.5z" fill="#888"/></svg>
      030 41 77 18 09
    </div>
    <div class="social"><span></span><span></span><span></span><span></span><span></span><span></span><span></span></div>
  </header>
  <nav class="nav">
    <a class="active">HOME</a><a>About Our firm</a><a>Funding Application</a><a>Invest with Bright Harbor</a><a>Our Process</a><a>Investment Profiles</a><a>Partner Profiles</a><a>Contact Us</a>
  </nav>
  <div class="tagline"><strong>Investments with impact</strong> will be the result of engaged, experienced business leaders<br>providing both capital and wisdom to entrepreneurs.</div>
  <div class="rule"></div>
  <section class="hero">
    <div class="hero-photo" role="img" aria-label="Photo of a smiling team of business people joining hands"></div>
    <div class="hero-copy">
      <h1>Funding and helping build<br><b>successful businesses</b></h1>
      <p>This will include a narrative about the target companies, how we work, the type of deals we are interested in, our expectations, etc ...</p>
      <div class="btn-orange">Learn more about us
        <svg viewBox="0 0 20 20"><circle cx="10" cy="10" r="10" fill="#fff"/><path d="M8 5.5l4.5 4.5L8 14.5" stroke="#222" stroke-width="2.4" fill="none"/></svg>
      </div>
    </div>
  </section>
</div>
<div class="hero-shadow"></div>

<section class="features">
  <div class="feature" style="left:13px"><div class="feature-head"><span class="feature-icon"></span><div class="feature-title">Funding application<small>Lorem Lipsum</small></div></div><p>Lorem Ipsum is simply dummy text of the printing and typeset-ting industry. Lorem Ipsum has been the industry's standard dummy text ever since the 1500s</p><span class="btn-gray">Read More</span></div>
  <div class="feature" style="left:174px"><div class="feature-head"><span class="feature-icon"></span><div class="feature-title">Investment<small>Lorem Lipsum</small></div></div><p>Lorem Ipsum is simply dummy text of the printing and typeset-ting industry. Lorem Ipsum has been the industry's standard dummy text ever since the 1500s</p><span class="btn-gray">Read More</span></div>
  <div class="feature" style="left:323px"><div class="feature-head"><span class="feature-icon"></span><div class="feature-title">Investment Profile<small>Lorem Lipsum</small></div></div><p>Lorem Ipsum is simply dummy text of the printing and typeset-ting industry. Lorem Ipsum has been the industry's standard dummy text ever since the 1500s</p><span class="btn-gray">Read More</span></div>
  <div class="feature" style="left:482px"><div class="feature-head"><span class="feature-icon"></span><div class="feature-title">Partner Profile<small>Lorem Lipsum</small></div></div><p>Lorem Ipsum is simply dummy text of the printing and typeset-ting industry. Lorem Ipsum has been the industry's standard dummy text ever since the 1500s</p><span class="btn-gray">Read More</span></div>
</section>

<div style="position:absolute;left:70px;top:0;width:623px">
  <div class="section-rule"></div>
  <h2 class="section-title" style="left:15px;top:728px">Latest Blog Posts</h2>
  <h2 class="section-title" style="left:408px;top:728px">Submit a Request</h2>
  <article class="post" style="left:16px"><div class="post-head"><div class="post-date"><span class="day">09</span><span class="mon">Aug</span></div><div class="post-title">Lorem Ipsum is simply dummy text of the</div></div><p>Lorem Ipsum is simply dummy text of the printing and typesetting industry. Lorem Ipsum has been the industry's standard dummy text ever since the 1500s, when an unknown printer took a galley of type and scrambled it to make a type specimen book.</p></article>
  <article class="post" style="left:214px"><div class="post-head"><div class="post-date"><span class="day">08</span><span class="mon">Aug</span></div><div class="post-title">Lorem Ipsum is simply dummy text of the</div></div><p>Lorem Ipsum is simply dummy text of the printing and typesetting industry. Lorem Ipsum has been the industry's standard dummy text ever since the 1500s, when an unknown printer took a galley of type and scrambled it to make a type specimen book.</p></article>
  <form class="request">
    <div class="field short">Name:</div>
    <div class="field short">Email:</div>
    <div class="field tall">Message:</div>
    <span class="btn-submit">SUBMIT</span>
  </form>
</div>

<footer class="footer">
  <div class="footer-col" style="left:18px">
    <h3>ABOUT US</h3>
    <p>Itaque earum rerum hic tenetur a sapiente delectus, ut aut reiciendis voluptatibus maiores alias consequatur aut perferendis doloribus asperiores repella.</p>
    <div style="height:14px"></div>
    <div class="contact-line"><b>Address:</b> No 518, Fernwood, Oregon</div>
    <div class="contact-line"><b>Phone:</b> 001 (480) 22 71 904</div>
    <div class="contact-line" style="border:none"><b>Email:</b> hello@brightharbor.example</div>
  </div>
  <div class="footer-col" style="left:232px">
    <h3>RECENT POSTS</h3>
    <ul class="recent">
      <li>› Pain that produces no resultant pleasure<small>September 27, 2013</small></li>
      <li>› Temporibus autem quibusdam<small>September 26, 2013</small></li>
      <li>› Debitis aut rerum necessitatibus saepe<small>September 25, 2013</small></li>
      <li>› Et voluptates repudiandae<small>September 22, 2013</small></li>
    </ul>
  </div>
  <div class="footer-col" style="left:444px;width:160px">
    <h3>LATEST TWEETS</h3>
    <div class="tweet"><span class="tweet-dot"></span><div>about 3 days ago 'Lumo - Multi Purpose Shop Layout' layouts.example/item/lumo-mul...</div></div>
    <div class="tweet"><span class="tweet-dot"></span><div>about 3 days ago 'Orin - OnePage Parallax Responsive HTML5 Layout' layouts.example/item/orin-one...</div></div>
    <div class="tweet"><span class="tweet-dot"></span><div>about 3 days ago 'Q - The Complete Site Builder Kit' layouts.example/item/q-the-com...</div></div>
  </div>
</footer>
<div class="copyright">Copyright © 2014 Bright Harbor Capital</div>
</body>
</html>
```